wardrobe/costume stylist needs good business card for own business

Hi:)

I'm wanting a business card for my company. I am a freelance stylist.

I do wardrobe/costume stylist to TV commercials; Films; Fashion and Lifestyle shoots.

I'd like a design based around my name Rosalind Pember written nicely, maybe a colour? Up to you?!

I've attached a couple of images of business cards I like
.... be creative and have fun!

Thank you :)
Updates

Reason: I was trying to get my new business card ready for before I headed overseas Friday morning but I don't think that was realistic so I'd like to extend the deadline to give time to the project. Thank you

Hi designers:) Thank you for all your designs, I've extended the deadline until Sunday, so there's a bit more time. I've attached 3 pictures of business cards which I quite like, please take a look to see if it can be of help in your process. I like the pale plain or patterned background with dark font and the dark plain or patterned background with the pale font the motifs the feminine fonts the plain fonts I like the idea of playing with a circle or some shape on one side of the card with my name or initials as in the picture I have on my post could you play around with this idea a bit please? Thank you all for the work you've done :) Rosa

Hi I am working overseas til Saturday night sorry for no feedback until I teturn Thanks :) Rosa

Hi designers, Thank you all so much for submitting your designs, I really appreciate your input into my project :) I'm sorry I didn't get to respond to some comments, and give feedback. I didn't back from being away until later than I expected, and the deadline had passed then, so apologies. Thanks to you all again for all your really good designs :) Rosa

Target Market(s)

I am a freelance stylist my target audience is producers, production companies, photographers, directors...

Industry/Entity Type

Business

Requirements
Must have
• Rosalind Pember
Stylist or Wardrobe Stylist

email rosapember@quillnet.co.nz
Mobile 0218846193

(Don't have to use the words 'email' and 'mobile')
Nice to have
• Would like it to be double sided
Like B & W
Like pale colour background with dark font or white font
Like dark colour background with pale font
Should not have
• I would prefer it not to incorporate pictures

```html
<!DOCTYPE html>
<html lang="en">
<head>
<meta charset="utf-8">
<title>Rosalind Pember – Business Card</title>
<link rel="stylesheet" href="https://fonts.googleapis.com/css2?family=Open+Sans:wght@400;600&display=swap">
<style>
  :root {
    --ink: #1d1918;
    --paper: #ffffff;
    --stage: #e4e4e4;
    --ghost: #dadada;
    --text: #222222;
  }
  * { box-sizing: border-box; margin: 0; padding: 0; }
  html, body { width: 1200px; height: 850px; overflow: hidden; }
  body {
    background: var(--stage);
    font-family: "Open Sans", Arial, sans-serif;
    position: relative;
  }
  .card {
    position: absolute;
    width: 500px;
    height: 290px;
    overflow: hidden;
  }
  /* Front side */
  .card--front {
    left: 90px;
    top: 120px;
    background: var(--ink);
  }
  .card--front .monogram {
    position: absolute;
    left: 120px;
    top: 70px;
    width: 150px;
    height: 150px;
    border-radius: 50%;
    background: var(--paper);
    display: flex;
    align-items: center;
    justify-content: center;
    text-align: center;
    color: var(--ink);
    font-weight: 600;
    font-size: 20px;
    line-height: 1.25;
  }
  /* Back side */
  .card--back {
    left: 610px;
    top: 440px;
    background: var(--paper);
  }
  .card--back .badge {
    position: absolute;
    left: 26px;
    top: 20px;
    width: 62px;
    height: 62px;
    border-radius: 50%;
    background: var(--ink);
    color: var(--paper);
    display: flex;
    align-items: center;
    justify-content: center;
    text-align: center;
    font-weight: 600;
    font-size: 9px;
    line-height: 1.2;
  }
  .card--back .name-ghost {
    position: absolute;
    right: 18px;
    top: 40px;
    color: var(--ghost);
    font-weight: 600;
    font-size: 50px;
    line-height: 1.05;
    text-align: right;
  }
  .card--back .details {
    position: absolute;
    left: 30px;
    top: 118px;
    color: var(--text);
    font-size: 13px;
    line-height: 1.55;
    list-style: none;
  }
  .details .detail { display: flex; align-items: center; gap: 7px; }
  .details .detail--plain { gap: 0; }
  .details svg { width: 12px; height: 12px; flex: none; }
  .card--back .edge-band {
    position: absolute;
    left: 0;
    right: 0;
    bottom: 0;
    height: 14px;
    background: var(--ink);
  }
</style>
</head>
<body>
  <section class="card card--front" aria-label="Card front">
    <div class="monogram">Rosalind<br>Pember</div>
  </section>

  <section class="card card--back" aria-label="Card back">
    <div class="badge">Rosalind<br>Pember</div>
    <div class="name-ghost" aria-hidden="true">Rosalind<br>Pember</div>
    <ul class="details">
      <li class="detail detail--plain">Rosalind Pember</li>
      <li class="detail detail--plain">Stylist or Wardrobe Stylist</li>
      <li class="detail">
        <svg viewBox="0 0 12 12" aria-hidden="true"><rect width="12" height="12" rx="1.5" fill="#1d1918"/><path d="M3.2 2.6c.4-.3.9-.2 1.1.2l.6 1.1c.2.4.1.8-.2 1l-.4.3c.3.8.9 1.5 1.7 1.9l.3-.4c.3-.3.7-.4 1-.2l1.1.6c.4.2.5.7.2 1.1l-.5.6c-.4.4-1 .5-1.5.3C4.8 8.4 3.5 7 2.9 5.3c-.2-.5 0-1.1.3-1.5z" fill="#fff"/></svg>
        0218846193
      </li>
      <li class="detail">
        <svg viewBox="0 0 12 12" aria-hidden="true"><rect width="12" height="12" rx="1.5" fill="#1d1918"/><rect x="2.2" y="3.4" width="7.6" height="5.2" fill="#fff"/><path d="M2.2 3.4L6 6.4l3.8-3" fill="none" stroke="#1d1918" stroke-width=".8"/></svg>
        rosapember@quillnet.co.nz
      </li>
      <li class="detail">
        <svg viewBox="0 0 12 12" aria-hidden="true"><rect width="12" height="12" rx="1.5" fill="#1d1918"/><path d="M6 2a2.6 2.6 0 0 0-2.6 2.6C3.4 6.6 6 10 6 10s2.6-3.4 2.6-5.4A2.6 2.6 0 0 0 6 2z" fill="#fff"/><circle cx="6" cy="4.6" r="1" fill="#1d1918"/></svg>
        48 harrow ln. 3rd floor NZ
      </li>
    </ul>
    <div class="edge-band"></div>
  </section>
</body>
</html>
```